Branded Flyer Template Libraries Brightmoor Funding

Create one-page flyer templates for equipment finance industry to provide a fast turnaround that consistent on-brand for educational and promotional flyers that can be quickly customized with partners logos. These will become a standard toolkit for marketing for use in Adobe Illustrator and editable. customer facing are business owners considering equipment financing typically used for leave behind flyers, email, and handouts. vendor facing to equipment dealers, manufacturers and sales reps who refer customers to us, typically used at trade shows, co branded flyers, and email promotions.
Requesting 1-2 flyer templates with concepts for educational, and promotional.
Brand guide and current flyers in circulation are uploaded as reference.
Look and feel
Each slider illustrates characteristics of the customer's brand and the style your logo design should communicate.

```html
<!DOCTYPE html>
<html lang="en">
<head>
<meta charset="utf-8">
<title>Brightmoor Funding – Equipment Finance Flyer</title>
<link href="https://fonts.googleapis.com/css2?family=Merriweather:wght@700;900&family=Montserrat:wght@400;500;600&display=swap" rel="stylesheet">
<style>
:root{
  --backdrop:#6d6d6d;
  --forest:#0f5a2a;
  --forest-deep:#0b4620;
  --leaf:#9cc46a;
  --leaf-soft:#a9c97a;
  --slate:#2c4a53;
  --ink:#1e2b30;
  --mist:#c4e6e5;
  --teal-dot:#6fb3ad;
  --white:#ffffff;
}
*{margin:0;padding:0;box-sizing:border-box}
html,body{width:981px;height:1200px;overflow:hidden}
body{background:var(--backdrop);font-family:"Montserrat",sans-serif;color:var(--ink)}
.flyer{position:absolute;left:40px;top:18px;width:900px;height:1164px;background:var(--white);overflow:hidden}
.abs{position:absolute}
.serif{font-family:"Merriweather",serif;font-weight:700}

.hero-band{left:0;top:210px;width:900px;height:237px;background:var(--forest)}
.hero-art{left:0;top:0}
.brand{left:0;top:0;width:378px;height:210px;text-align:center}
.brand-mark{position:absolute;left:162px;top:48px;width:56px;height:56px;border-radius:50%;background:var(--forest)}
.brand-name{position:absolute;left:0;top:140px;width:378px;font-family:"Merriweather",serif;font-weight:700;font-size:23px;color:var(--forest);letter-spacing:.3px}
.brand-tag{position:absolute;left:0;top:178px;width:378px;font-size:8.5px;font-weight:600;letter-spacing:3px;color:var(--ink)}
.brand-tag span{display:inline-block;width:22px;height:1px;background:var(--ink);vertical-align:middle;margin:0 8px}

.headline{left:51px;top:223px;font-family:"Merriweather",serif;font-weight:900;font-size:60px;line-height:67px;color:var(--white)}
.headline .accent{color:var(--leaf)}

h2{font-family:"Merriweather",serif;font-weight:700;color:var(--slate)}
.about-title{left:51px;top:452px;font-size:21px}
.about-text{left:51px;top:486px;width:405px;font-size:11.3px;line-height:15px}
.team-photo{left:51px;top:594px;width:389px;height:162px;border-radius:10px;background:linear-gradient(180deg,#3f6a34 0%,#5a7a4a 45%,#6a6a78 75%,#9aa098 100%)}
.why-title{left:51px;top:772px;font-size:21px}
.why-text{left:51px;top:810px;width:330px;font-size:11.3px;line-height:15px}
.ticks{left:51px;top:851px;width:400px;display:grid;grid-template-columns:186px 186px;row-gap:12px;font-size:11px;line-height:15px}
.ticks li{list-style:none;position:relative;padding-left:15px}
.ticks li::before{content:"";position:absolute;left:0;top:4px;width:9px;height:9px;border-radius:50%;background:var(--teal-dot)}
.divider{left:51px;top:940px;width:389px;height:1px;background:#9aa7ab}
.highlight{top:960px;width:140px}
.highlight .num{position:absolute;left:0;top:0;width:43px;height:43px;border-radius:50%;border:3px solid var(--mist);font-family:"Merriweather",serif;font-weight:700;font-size:17px;color:var(--slate);display:flex;align-items:center;justify-content:center}
.highlight .label{position:absolute;left:50px;top:2px;font-family:"Merriweather",serif;font-weight:700;font-size:15px;line-height:18px;color:var(--slate)}
.highlight p{position:absolute;left:1px;top:57px;width:118px;font-size:11px;line-height:14px}

.footer{left:0;top:1069px;width:900px;height:95px;background:var(--slate)}
.contact-item{top:1085px;display:flex;align-items:center;gap:9px;color:var(--white);font-weight:500;font-size:14px;white-space:nowrap}
.contact-item .ico{width:25px;height:25px;border-radius:50%;background:var(--mist);display:flex;align-items:center;justify-content:center}

.panel-head{left:503px;top:467px;width:347px;height:46px;background:var(--leaf-soft);border-radius:6px 6px 0 0;padding:9px 0 0 36px;font-size:21px;color:var(--slate)}
.panel{left:503px;top:517px;width:347px;height:605px;background:var(--mist);border-radius:0 0 8px 8px}
.ability{left:488px;width:360px}
.ability .badge{position:absolute;left:0;top:0;width:36px;height:36px;border-radius:50%;background:var(--slate);border:3px solid #e3f3f2;display:flex;align-items:center;justify-content:center}
.ability h3{position:absolute;left:51px;top:4px;font-family:"Merriweather",serif;font-weight:700;font-size:15px;color:var(--slate)}
.ability p{position:absolute;left:51px;top:34px;width:282px;font-size:11px;line-height:15px}
.rule{left:539px;width:290px;border-top:1px dashed #3b5a62}
</style>
</head>
<body>
<div class="flyer">

  <div class="abs hero-band"></div>

  <svg class="abs hero-art" width="900" height="447" viewBox="0 0 900 447">
    <defs>
      <linearGradient id="photoTone" x1="0" y1="0" x2="1" y2="1">
        <stop offset="0" stop-color="#d9d6d0"/>
        <stop offset=".45" stop-color="#8a8a90"/>
        <stop offset=".75" stop-color="#4a4f5e"/>
        <stop offset="1" stop-color="#b8ab98"/>
      </linearGradient>
    </defs>
    <polygon points="299,0 536,0 426,199" fill="#a8cc7c" role="img" aria-label="Two farm workers talking in a green field, tinted green"/>
    <polygon points="536,0 900,0 900,447 560,447 440,222" fill="#0d4d23"/>
    <polyline points="555,0 447,222 565,447" fill="none" stroke="#9cc46a" stroke-width="7"/>
    <polyline points="566,0 458,222 575,447" fill="none" stroke="#ffffff" stroke-width="3"/>
    <polygon points="572,0 900,0 900,447 582,447 464,222" fill="url(#photoTone)" role="img" aria-label="A finance advisor with a tablet talking to a farmer beside a tractor tyre and red farm equipment"/>
  </svg>

  <div class="abs brand">
    <div class="brand-mark"></div>
    <div class="brand-name">BRIGHTMOOR FUNDING</div>
    <div class="brand-tag"><span></span>EQUIPMENT FINANCE<span></span></div>
  </div>

  <div class="abs headline">Financing<br>That Flexes<br><span class="accent">With You</span></div>

  <h2 class="abs about-title">About us</h2>
  <p class="abs about-text">Lorem Ipsum is simply dummy text of the printing &amp; typesetting industry. Lorem Ipsum has been the industry's standard dummy text ever since 1966, when designers at Fernwick Type and Harlan Odell, the librarian at Ashgrove Printing Library in Dunmere, took a 1914 classical translation and scrambled it to make dummy text for Fernwick's Body Type sheets.</p>

  <div class="abs team-photo" role="img" aria-label="Group photo of the company team standing outdoors on a lawn"></div>

  <h2 class="abs why-title">Why Choose Us ?</h2>
  <p class="abs why-text">Lorem Ipsum is simply dummy text of the printing &amp; typesetting industry.</p>
  <ul class="abs ticks">
    <li>Lorem ipsus sinctio riatent ulluptae nis ium sedit</li>
    <li>Lorem ipsus sinctio riatent ulluptae nis ium sedit</li>
    <li>Lorem ipsus sinctio riatent ulluptae nis ium sedit</li>
    <li>Lorem ipsus sinctio riatent ulluptae nis ium sedit</li>
  </ul>

  <div class="abs divider"></div>

  <div class="abs highlight" style="left:51px">
    <div class="num">01</div><div class="label">Highlight<br>One</div>
    <p>Lorem ipsus sinctio riatent ulluptae nis ium sedit</p>
  </div>
  <div class="abs highlight" style="left:187px">
    <div class="num">02</div><div class="label">Highlight<br>Two</div>
    <p>Lorem ipsus sinctio riatent ulluptae nis ium sedit</p>
  </div>
  <div class="abs highlight" style="left:325px">
    <div class="num">03</div><div class="label">Highlight<br>Three</div>
    <p>Lorem ipsus sinctio riatent ulluptae nis ium sedit</p>
  </div>

  <div class="abs footer"></div>
  <div class="abs contact-item" style="left:50px">
    <span class="ico"><svg width="13" height="13" viewBox="0 0 24 24"><path d="M6.6 10.8a15 15 0 0 0 6.6 6.6l2.2-2.2a1 1 0 0 1 1-.25 11.4 11.4 0 0 0 3.6.6 1 1 0 0 1 1 1V20a1 1 0 0 1-1 1A17 17 0 0 1 3 4a1 1 0 0 1 1-1h3.5a1 1 0 0 1 1 1c0 1.25.2 2.45.6 3.6a1 1 0 0 1-.25 1z" fill="#2c4a53"/></svg></span>
    <span>(800) 555-0148</span>
  </div>
  <div class="abs contact-item" style="left:213px">
    <span class="ico"><svg width="15" height="15" viewBox="0 0 24 24" fill="none" stroke="#2c4a53" stroke-width="2"><circle cx="12" cy="12" r="9"/><path d="M3 12h18M12 3c3 3.5 3 14.5 0 18M12 3c-3 3.5-3 14.5 0 18"/></svg></span>
    <span>www.brightmoorfunding.com</span>
  </div>

  <div class="abs panel"></div>
  <div class="abs panel-head serif">Partner-abilities</div>

  <div class="abs ability" style="top:536px">
    <div class="badge"><svg width="16" height="16" viewBox="0 0 24 24" fill="#fff"><circle cx="9" cy="7" r="3"/><path d="M3 20v-3a6 6 0 0 1 12 0v3zM16 8h6v7h-6z"/></svg></div>
    <h3>Industry Experts</h3>
    <p>Lorem Ipsum is simply dummy text of the printing &amp; typesetting industry.</p>
  </div>
  <div class="abs rule" style="top:615px"></div>

  <div class="abs ability" style="top:637px">
    <div class="badge"><svg width="16" height="16" viewBox="0 0 24 24" fill="#fff"><path d="M4 13h4l5 3h6v3H12l-8-2zM12 4h8v7h-8z"/></svg></div>
    <h3>People Who Deliver</h3>
    <p>Lorem Ipsum is simply dummy text of the printing &amp; typesetting industry.</p>
  </div>
  <div class="abs rule" style="top:718px"></div>

  <div class="abs ability" style="top:738px">
    <div class="badge"><svg width="16" height="16" viewBox="0 0 24 24" fill="none" stroke="#fff" stroke-width="2"><path d="M3 10a13 13 0 0 1 18 0M6 13.5a8.5 8.5 0 0 1 12 0M9 17a4 4 0 0 1 6 0"/><circle cx="12" cy="20" r="1" fill="#fff"/></svg></div>
    <h3>Speed That Wins</h3>
    <p>Lorem Ipsum is simply dummy text of the printing &amp; typesetting industry.</p>
  </div>
  <div class="abs rule" style="top:818px"></div>

  <div class="abs ability" style="top:838px">
    <div class="badge"><svg width="16" height="16" viewBox="0 0 24 24" fill="none" stroke="#fff" stroke-width="2"><circle cx="12" cy="9" r="5"/><path d="M9 13l-2 8 5-3 5 3-2-8"/></svg></div>
    <h3>Proven Value</h3>
    <p>Lorem Ipsum is simply dummy text of the printing &amp; typesetting industry.</p>
  </div>
  <div class="abs rule" style="top:914px"></div>

  <div class="abs ability" style="top:934px">
    <div class="badge"><svg width="16" height="16" viewBox="0 0 24 24" fill="#fff"><path d="M3 20V11l5 3V11l5 3V6h3v14zM18 3h2v17h-2z"/></svg></div>
    <h3>Powering Your Sales</h3>
    <p>Lorem Ipsum is simply dummy text of the printing &amp; typesetting industry.</p>
  </div>
  <div class="abs rule" style="top:1011px"></div>

  <div class="abs ability" style="top:1029px">
    <div class="badge"><svg width="16" height="16" viewBox="0 0 24 24" fill="none" stroke="#fff" stroke-width="2"><path d="M6 3h9l4 4v14H6z"/><path d="M9 14l2 2 4-4"/></svg></div>
    <h3>Approvals That Move</h3>
    <p>Lorem Ipsum is simply dummy text of the printing &amp; typesetting industry.</p>
  </div>

</div>
</body>
</html>
```